Concept Web Design - Motivational Speaker

Update 4.4.18 --- Website references to use for inspiration or ideas:
http :// tovanbrisk . com
https :// peakrally . com

Navigation Bar:
- Home
- About
- Speaking
- Book Nessa
- Video
- Testimonials
- Blog
- Books
- Giving Back

Home Page (done in sections with images included):
- Style Details: Fun, professional, sports-theme. Turf as background
- Colors – Main color should be grass like with 1 or 2 complimentary colors

- 1st Section Text (Intro):
o Nessa Pruitt is the owner of Over the Goal Post and author of hundreds of children’s activity books, storybooks, and adult coloring books for sports teams, leagues, and brands. Pruitt started with a blank piece of paper and a desire to make a child smile. In 2011, one of her marketing clients’ sons was struck by a car and he broke both of his legs. Pruitt knew that he loved Crimson Valley football so she stayed up until 3 a.m. crafting the first-ever Bend Creek Puzzle Book as a gift for him. She has grown her business and expanded her line to include 39 UCLV teams, 32 GRL teams, 30 PHS teams, 30 DVK teams, a non-licensed sports line, and non-sports titles. She donates activity books to children in local hospitals as she makes business visits across the country. She is driven with a purpose and that is to create champions in education and sports, while making an impact on those around her.

Read more….

- 2nd Section Text:
o Nessa Pruitt was born in Ashby Ford, Westmarch. She grew up in the Quiet Porch of Millbrook Hollow, Westmarch, not far from Kessington, where Wade Tiller Ostrander was born and sings about. Her parents were instrumental in teaching her to be a strong and independent woman. She was often told that dynamite comes in small packages because she has so much energy and lights up any room she is in. The song, “Quiet Porch” was one that she grew up listening to.

Read more…

- 3rd Section Text:
o Video Clip Preview (still images)
o Brief Description
o Link To Video Page
- 4th Section:
o Testimonials

Read more…

- 5th Section:
o Recent Blog Posts
- 6th Section:
o Brief preview of books written by Nessa
o Link to Book page
- 7th Section:
o Nessa Pruitt enjoys giving back to children in hospitals. She travels around the country donating her activity books to children and building special bonds with them

Read more…

- Footer
o Contact info
o Social media
o Copyright, etc..

Target Market(s)

Businesses and Corporations

Industry/Entity Type

Motivation

Number of Pages Required

5+ page

Requirements
Must have
• Everything in the product description.

```html
<!DOCTYPE html>
<html lang="en">
<head>
<meta charset="utf-8">
<title>Nessa Pruitt – Motivational Speaker</title>
<link rel="stylesheet" href="https://fonts.googleapis.com/css2?family=Open+Sans:wght@400;600;700;800&display=swap">
<style>
:root{
  --green:#7cc11f;
  --ink:#1d1d1d;
  --body:#555;
  --muted:#888;
  --light:#ececec;
  --white:#fff;
  --social-1:#2b4f9c;
  --social-2:#2fa3e0;
  --social-3:#1f5e8f;
}
*{box-sizing:border-box;margin:0;padding:0}
html,body{width:1200px;height:4852px;overflow:hidden}
body{font-family:"Open Sans",Arial,sans-serif;color:var(--ink);background:var(--white);position:relative}
.section{position:absolute;left:0;width:1200px;overflow:hidden}
.fill{position:absolute}
.btn{display:inline-block;background:var(--green);color:var(--white);font-weight:700;font-size:14px;letter-spacing:.5px;padding:10px 22px;text-transform:uppercase;text-decoration:none}
.btn.small{font-size:10px;padding:6px 12px}
.heading{font-weight:800;font-size:30px;text-transform:uppercase;letter-spacing:.5px;color:var(--ink)}
.copy{font-size:11.5px;line-height:1.62;color:var(--body)}
.abs{position:absolute}

/* hero */
.hero{top:0;height:695px}
.hero .fill{inset:0;background:linear-gradient(100deg,#2f5a16 0%,#4f8a22 40%,#3d6f1a 70%,#22410e 100%)}
.hero .speaker{position:absolute;left:600px;top:70px;width:330px;height:625px;background:linear-gradient(180deg,#d9c38a 0%,#eeeeee 35%,#222 80%)}
.topbar{position:absolute;top:0;left:0;width:1200px;height:58px;background:rgba(0,0,0,.55)}
.brand{position:absolute;left:130px;top:0;line-height:58px;color:var(--white);font-weight:800;font-size:22px;letter-spacing:1px}
.nav{position:absolute;left:346px;top:0;height:58px;display:flex}
.nav a{color:var(--white);text-decoration:none;font-size:12px;font-weight:600;text-transform:uppercase;padding:0 15px;line-height:58px}
.nav a.active{background:var(--green)}
.hero-title{position:absolute;left:204px;top:240px;color:var(--white);font-weight:800;line-height:1.05}
.hero-title .small{display:block;font-size:38px}
.hero-title .big{display:block;font-size:58px}
.hero .read{position:absolute;left:204px;top:395px;background:#e6e6e6;color:var(--ink);font-weight:700;font-size:14px;padding:8px 18px;text-decoration:none}
.dots{position:absolute;left:210px;top:528px;display:flex;gap:14px}
.dots span{width:9px;height:9px;border-radius:50%;background:rgba(255,255,255,.75)}

/* welcome */
.welcome{top:695px;height:518px;background:var(--white)}
.welcome .fill{left:0;top:0;width:615px;height:518px;background:linear-gradient(135deg,#8a6a4a,#5a4330 55%,#d8d0c4)}

/* about */
.about{top:1213px;height:572px;background:var(--light)}
.about .fill{left:624px;top:0;width:576px;height:572px;background:linear-gradient(160deg,#8e8a82,#4d4a45 60%,#2a2826)}
.about .card{position:absolute;left:220px;top:162px;width:446px;height:323px;background:var(--white);box-shadow:0 6px 24px rgba(0,0,0,.18);padding:44px 60px}

/* videos */
.videos{top:1785px;height:560px;background:var(--white)}
.videos .fill{left:0;top:0;width:624px;height:560px;background:linear-gradient(135deg,#2b3c7a,#b8233a 45%,#d8d8d8 70%,#26335f)}

/* testimonials */
.testimonials{top:2345px;height:556px}
.testimonials .fill{inset:0;background:linear-gradient(180deg,#5a2e28,#7b3f33 50%,#4a2420)}
.testimonials .shade{position:absolute;inset:0;background:rgba(0,0,0,.45)}
.quote-mark{position:absolute;color:var(--white);font-size:72px;font-weight:800;font-family:Georgia,serif;line-height:1}
.arrow{position:absolute;top:240px;width:42px;height:42px;border:2px solid var(--white);border-radius:50%}
.arrow svg{position:absolute;left:12px;top:12px}

/* blog */
.blog{top:2901px;height:624px;background:var(--white)}
.post{position:absolute;top:155px;width:278px}
.post .thumb{height:188px}
.post .date{font-size:10px;color:var(--muted);margin-top:28px}
.post h3{font-size:15px;font-weight:700;margin-top:4px}
.post p{font-size:11px;line-height:1.6;color:var(--body);margin-top:10px}
.post .btn{margin-top:12px}

/* books */
.books{top:3525px;height:518px;background:var(--light)}
.books .cover{position:absolute;left:194px;top:71px;width:307px;height:447px;background:linear-gradient(180deg,#c52a46,#8e1b31 55%,#b7b7b7)}
.books .spread{position:absolute;left:922px;top:291px;width:278px;height:227px;background:linear-gradient(160deg,#f4f4f4,#c9c9c9)}

/* giving back */
.giving{top:4043px;height:420px}
.giving .fill{inset:0;background:linear-gradient(110deg,#3b2a22,#6a5444 50%,#2c2420)}
.giving .shade{position:absolute;inset:0;background:rgba(0,0,0,.35)}

/* footer */
.footer{top:4463px;height:389px;background:var(--white)}
.footer .sketch{position:absolute;left:0;top:20px;width:390px;height:330px;background:linear-gradient(180deg,#f4f4f4,#fafafa)}
.footer .logo{position:absolute;left:135px;top:130px;color:var(--green);font-weight:800;font-size:32px;letter-spacing:1px}
.footer h4{font-size:12px;font-weight:800;text-transform:uppercase;margin-bottom:16px}
.footer ul{list-style:none;font-size:11px;color:var(--body);line-height:1.55}
.contact li{display:flex;gap:10px;margin-bottom:14px;align-items:flex-start}
.social li{display:flex;align-items:center;gap:10px;margin-bottom:14px}
.social .dot{width:24px;height:24px;border-radius:50%}
.copyright{position:absolute;left:0;width:1200px;top:332px;text-align:center;font-size:11px;color:var(--body)}
</style>
</head>
<body>

<section class="section hero">
  <div class="fill" role="img" aria-label="Turf field background"></div>
  <div class="speaker" role="img" aria-label="Photo of Nessa Pruitt standing in a white blazer"></div>
  <header class="topbar">
    <div class="brand">NESSA PRUITT</div>
    <nav class="nav">
      <a class="active" href="#">Home</a><a href="#">About</a><a href="#">Speaking</a><a href="#">Book Nessa</a><a href="#">Video</a><a href="#">Testimonials</a><a href="#">Blog</a><a href="#">Books</a><a href="#">Giving Back</a>
    </nav>
  </header>
  <h1 class="hero-title"><span class="small">WELCOME TO</span><span class="big">NESSA PRUITT</span></h1>
  <a class="read" href="#">READ MORE</a>
  <div class="dots"><span></span><span></span><span></span><span></span><span></span></div>
</section>

<section class="section welcome">
  <div class="fill" role="img" aria-label="Photo of Nessa posing beside a bronze bull statue"></div>
  <h2 class="heading abs" style="left:702px;top:66px">Welcome!</h2>
  <p class="copy abs" style="left:702px;top:118px;width:430px">Nessa Pruitt is the owner of <em>Over the Goal Post</em> and author of hundreds of children's activity books, storybooks, and adult coloring books for sports teams, leagues, and brands. Pruitt started with a blank piece of paper and a desire to make a child smile. In 2011, one of her marketing clients' sons was struck by a car and he broke both of his legs. Pruitt knew that he loved Crimson Valley football so she stayed up until 3 a.m. crafting the first-ever Bend Creek Puzzle Book as a gift for him. She has grown her business and expanded her line to include 39 UCLV teams, 32 GRL teams, 30 PHS teams, 30 DVK teams, a non-licensed sports line, and non-sports titles. She donates activity books to children in local hospitals as she makes business visits across the country. She is driven with a purpose and that is to create champions in education and sports, while making an impact on those around her.</p>
  <a class="btn abs" style="left:702px;top:385px" href="#">Read More</a>
</section>

<section class="section about">
  <div class="fill" role="img" aria-label="Photo of Nessa seated on a stone ledge"></div>
  <h2 class="heading abs" style="left:220px;top:98px">About Nessa</h2>
  <div class="card">
    <p class="copy">Nessa Pruitt was born in Ashby Ford, Westmarch. She grew up in the Quiet Porch of Millbrook Hollow, Westmarch, not far from Kessington, where Wade Tiller Ostrander was born and sings about. Her parents were instrumental in teaching her to be a strong and independent woman. She was often told that dynamite comes in small packages because she has so much energy and lights up any room she is in. The song, "Quiet Porch" was one that she grew up listening to.</p>
    <a class="btn" style="margin-top:24px;margin-left:30px" href="#">Read More</a>
  </div>
</section>

<section class="section videos">
  <div class="fill" role="img" aria-label="Video still of Nessa speaking on stage"></div>
  <h2 class="heading abs" style="left:718px;top:123px">Videos</h2>
  <p class="copy abs" style="left:718px;top:175px;width:420px">Sed ut perspiciatis unde omnis iste natus error sit voluptatem accusantium doloremque laudantium, totam rem aperiam, eaque ipsa quae ab illo inventore veritatis et quasi architecto beatae vitae dicta sunt explicabo. Nemo enim ipsam voluptatem quia voluptas sit aspernatur aut odit aut fugit, sed quia consequuntur magni dolores eos qui ratione voluptatem sequi nesciunt. Neque porro quisquam est, qui dolorem ipsum quia dolor sit amet, consectetur, adipisci velit, sed quia non numquam eius modi tempora incidunt ut labore et dolore magnam.</p>
  <a class="btn abs" style="left:718px;top:378px" href="#">Watch Video</a>
</section>

<section class="section testimonials">
  <div class="fill" role="img" aria-label="Crowd of fans in a stadium"></div>
  <div class="shade"></div>
  <h2 class="heading abs" style="left:0;width:1200px;top:72px;text-align:center;color:var(--white)">Testimonials</h2>
  <div class="quote-mark" style="left:300px;top:168px">&ldquo;</div>
  <p class="abs" style="left:330px;top:206px;width:540px;text-align:center;color:var(--white);font-size:13px;line-height:1.6">Sed ut perspiciatis unde omnis iste natus error sit voluptatem accusantium doloremque laudantium, totam rem aperiam, eaque ipsa quae ab illo inventore veritatis et quasi architecto beatae vitae dicta sunt explicabo. Nemo enim ipsam voluptatem quia voluptas sit aspernatur aut odit aut fugit, sed quia consequuntur magni dolores eos qui ratione voluptatem sequi nesciunt. Neque porro</p>
  <div class="quote-mark" style="left:826px;top:300px">&rdquo;</div>
  <p class="abs" style="left:0;width:1200px;top:392px;text-align:center;color:var(--white);font-size:11px"><strong>Colin Arvane</strong>, Australia</p>
  <span class="arrow" style="left:164px"><svg width="14" height="14" viewBox="0 0 14 14"><path d="M9 2 L4 7 L9 12" stroke="#fff" stroke-width="2" fill="none"/></svg></span>
  <span class="arrow" style="left:990px"><svg width="14" height="14" viewBox="0 0 14 14"><path d="M5 2 L10 7 L5 12" stroke="#fff" stroke-width="2" fill="none"/></svg></span>
  <a class="btn abs" style="left:535px;top:462px" href="#">Read More</a>
</section>

<section class="section blog">
  <h2 class="heading abs" style="left:0;width:1200px;top:58px;text-align:center">Recent Blog</h2>
  <article class="post" style="left:133px">
    <div class="thumb" role="img" aria-label="Photo of Nessa in a red cap" style="background:linear-gradient(135deg,#2a62b8,#c2323a 50%,#e8d4b4)"></div>
    <div class="date">Mar 26, 2018</div>
    <h3>Sed ut perspiciatis unde omnis iste</h3>
    <p>But I must explain to you how all this mistaken idea of denouncing pleasure and praising pain was born and I will give you a complete.</p>
    <a class="btn small" href="#">Read More</a>
  </article>
  <article class="post" style="left:459px">
    <div class="thumb" role="img" aria-label="Photo of Nessa holding a sports activity book" style="background:linear-gradient(135deg,#b89b86,#c9405a 55%,#f0e6e0)"></div>
    <div class="date">Mar 26, 2018</div>
    <h3>Sed ut perspiciatis unde omnis iste</h3>
    <p>But I must explain to you how all this mistaken idea of denouncing pleasure and praising pain was born and I will give you a complete.</p>
    <a class="btn small" href="#">Read More</a>
  </article>
  <article class="post" style="left:786px">
    <div class="thumb" role="img" aria-label="Photo of Nessa with children reading books" style="background:linear-gradient(135deg,#6f5a4a,#c9a888 50%,#3f6e8f)"></div>
    <div class="date">Mar 26, 2018</div>
    <h3>Sed ut perspiciatis unde omnis iste</h3>
    <p>But I must explain to you how all this mistaken idea of denouncing pleasure and praising pain was born and I will give you a complete.</p>
    <a class="btn small" href="#">Read More</a>
  </article>
</section>

<section class="section books">
  <div class="cover" role="img" aria-label="Cover of the Bend Creek Puzzle Book"></div>
  <h2 class="heading abs" style="left:598px;top:92px;font-size:20px">Books Written by Nessa</h2>
  <p class="copy abs" style="left:598px;top:132px;width:420px">Sed ut perspiciatis unde omnis iste natus error sit voluptatem accusantium doloremque laudantium, totam rem aperiam, eaque ipsa quae ab illo inventore veritatis et quasi architecto beatae vitae dicta sunt explicabo. Nemo enim ipsam voluptatem quia voluptas sit aspernatur aut odit aut fugit, sed quia consequuntur magni dolores eos qui ratione voluptatem sequi nesciunt. Neque porro quisquam est, qui dolorem ipsum quia dolor sit amet, consectetur, adipisci velit, sed quia non numquam eius modi tempora incidunt ut labore et dolore magnam</p>
  <a class="btn abs" style="left:598px;top:320px" href="#">View Book</a>
  <div class="spread" role="img" aria-label="Open activity book pages"></div>
</section>

<section class="section giving">
  <div class="fill" role="img" aria-label="Children reading activity books in a hospital"></div>
  <div class="shade"></div>
  <p class="abs" style="left:0;width:1200px;top:118px;text-align:center;color:var(--white);font-size:21px;font-weight:700;line-height:1.5">Nessa Pruitt enjoys giving back to children in hospitals.<br>She travels around the country donating her activity books to<br>children and building special bonds with them</p>
  <a class="btn abs" style="left:535px;top:272px" href="#">Read More</a>
</section>

<footer class="section footer">
  <div class="sketch" role="img" aria-label="Line sketch of Nessa"></div>
  <div class="logo">NESSA PRUITT</div>
  <div class="abs contact" style="left:475px;top:62px">
    <h4>Contact Us</h4>
    <ul>
      <li><svg width="12" height="14" viewBox="0 0 12 14"><path d="M6 0a5 5 0 0 1 5 5c0 4-5 9-5 9S1 9 1 5a5 5 0 0 1 5-5z" fill="#333"/><circle cx="6" cy="5" r="2" fill="#fff"/></svg><span>218 Meadowline Road<br>Fairbrook, WM 60999</span></li>
      <li><svg width="12" height="12" viewBox="0 0 12 12"><path d="M2 1l2.5 0 1 3-1.5 1a7 7 0 0 0 3 3l1-1.5 3 1V11c-5 0-9-4-9-9z" fill="#333"/></svg><span>555.010.2040</span></li>
      <li><svg width="13" height="10" viewBox="0 0 13 10"><rect x="0.5" y="0.5" width="12" height="9" fill="none" stroke="#333"/><path d="M.5 .5 6.5 5.5 12.5 .5" fill="none" stroke="#333"/></svg><span>hello@nessapruitt.example</span></li>
    </ul>
  </div>
  <div class="abs" style="left:731px;top:62px">
    <h4>Menu</h4>
    <ul><li>Home</li><li>About</li><li>Speaking</li><li>Book Nessa</li><li>Video</li><li>Testimonials</li><li>Blog</li><li>Books</li><li>Giving Back</li></ul>
  </div>
  <div class="abs social" style="left:935px;top:62px">
    <h4>Connect With Us</h4>
    <ul>
      <li><span class="dot" style="background:var(--social-1)"></span>Friendpage</li>
      <li><span class="dot" style="background:var(--social-2)"></span>Chirpline</li>
      <li><span class="dot" style="background:var(--social-3)"></span>Workgraph</li>
    </ul>
  </div>
  <p class="copyright">Copyright @ 2018 All Rights Reserved</p>
</footer>

</body>
</html>
```